Business Card Design for Business Broker

Hi - I am looking for a cool design for my new business card using the logo attached.

We are business brokers. We help people buy and sell businesses!

I am open to just about anything. As far as colors, I do like the navy blue that is part of my logo.

Industry/Entity Type

Business

```html
<!DOCTYPE html>
<html lang="en">
<head>
<meta charset="utf-8">
<title>Harland Moss – Business Card</title>
<link rel="stylesheet" href="https://fonts.googleapis.com/css2?family=Marcellus&family=Open+Sans:wght@400&family=Cormorant+Garamond:wght@500&display=swap">
<style>
  :root{
    --navy:#16164f;
    --navy-deep:#0f0f3d;
    --navy-soft:#1d1d62;
    --paper:#ffffff;
    --paper-shade:#f1f1f1;
    --ink:#1a1a1a;
    --ink-soft:#555555;
    --backdrop:#3b3b3d;
    --rule:#2a2a6a;
  }
  *{box-sizing:border-box;margin:0;padding:0}
  html,body{width:1200px;height:1000px;overflow:hidden}
  body{background:var(--backdrop);position:relative;font-family:"Open Sans",sans-serif}

  .card{position:absolute;top:150px;width:400px;height:700px;overflow:hidden;box-shadow:0 10px 30px rgba(0,0,0,.35)}

  /* Front */
  .card-front{left:150px;background:radial-gradient(ellipse at 55% 40%,var(--navy-soft),var(--navy-deep) 80%)}
  .card-front .brand{position:absolute;top:130px;left:0;right:0;text-align:center;color:#e9e9f2}
  .brand-name{font-family:"Marcellus",serif;font-size:34px;letter-spacing:2px;line-height:1}
  .brand-tagline{font-family:"Cormorant Garamond",serif;font-weight:500;font-size:17px;letter-spacing:.5px;margin-top:6px}
  .card-front .website{position:absolute;left:36px;bottom:40px;font-family:"Cormorant Garamond",serif;font-weight:500;font-size:20px;color:#d8d8e6;letter-spacing:1px}

  /* Back */
  .card-back{left:650px;background:linear-gradient(160deg,var(--paper) 40%,var(--paper-shade))}
  .card-back .brand{position:absolute;top:44px;right:34px;text-align:right;color:var(--navy)}
  .card-back .brand-name{font-size:32px}
  .card-back .brand-tagline{font-size:16px;color:var(--ink-soft)}

  .person{position:absolute;top:150px;left:40px}
  .person-name{font-family:"Cormorant Garamond",serif;font-weight:500;font-size:21px;letter-spacing:1px;color:var(--ink)}
  .person-role{font-size:10px;color:var(--ink-soft);margin-top:1px}

  .contact-list{position:absolute;top:218px;left:40px;width:326px;list-style:none}
  .contact-item{position:relative;height:70px}
  .contact-text{font-size:12.5px;letter-spacing:1px;color:#444;line-height:1.45;padding-top:4px}
  .contact-rule{position:absolute;left:0;right:36px;top:46px;height:1.5px;background:var(--rule)}
  .contact-icon{position:absolute;right:0;top:30px;width:34px;height:34px;background:var(--navy)}
  .contact-icon svg{display:block;width:34px;height:34px}

  .back-swoosh{position:absolute;left:0;bottom:0;width:400px;height:200px}
</style>
</head>
<body>

  <section class="card card-front" aria-label="Card front">
    <div class="brand">
      <div class="brand-name">HARLAND MOSS</div>
      <div class="brand-tagline">Business Brokers &amp; Consultants</div>
    </div>
    <div class="website">www.Yourweb.com</div>
  </section>

  <section class="card card-back" aria-label="Card back">
    <div class="brand">
      <div class="brand-name">HARLAND MOSS</div>
      <div class="brand-tagline">Business Brokers &amp; Consultants</div>
    </div>

    <div class="person">
      <div class="person-name">YOUR NAME</div>
      <div class="person-role">Owner</div>
    </div>

    <ul class="contact-list">
      <li class="contact-item">
        <div class="contact-text">4710 Cedar Ln.<br>Your address ,City 40810</div>
        <span class="contact-rule"></span>
        <span class="contact-icon"><svg viewBox="0 0 34 34"><path d="M17 8a6 6 0 0 0-6 6c0 5 6 12 6 12s6-7 6-12a6 6 0 0 0-6-6z" fill="#fff"/><circle cx="17" cy="14" r="2.2" fill="#16164f"/></svg></span>
      </li>
      <li class="contact-item">
        <div class="contact-text">555-201-4418<br>555-201-4418</div>
        <span class="contact-rule"></span>
        <span class="contact-icon"><svg viewBox="0 0 34 34"><path d="M9 13c0-3 4-4 8-4s8 1 8 4v2h-4v-2h-8v2H9z" fill="#fff"/><rect x="11" y="16" width="12" height="9" rx="1.5" fill="#fff"/><circle cx="17" cy="20.5" r="2" fill="#16164f"/></svg></span>
      </li>
      <li class="contact-item">
        <div class="contact-text">123-345-879</div>
        <span class="contact-rule"></span>
        <span class="contact-icon"><svg viewBox="0 0 34 34"><rect x="13" y="8" width="10" height="7" fill="#fff"/><rect x="8" y="14" width="18" height="12" rx="1.5" fill="#fff"/><rect x="11" y="17" width="7" height="6" fill="#16164f"/><rect x="20" y="17" width="3" height="2" fill="#16164f"/><rect x="20" y="21" width="3" height="2" fill="#16164f"/></svg></span>
      </li>
      <li class="contact-item">
        <div class="contact-text">admin@yourweb.com<br>www.yourweb.com</div>
        <span class="contact-rule"></span>
        <span class="contact-icon"><svg viewBox="0 0 34 34"><rect x="8" y="9" width="18" height="12" rx="1" fill="#fff"/><rect x="10" y="11" width="14" height="8" fill="#16164f"/><rect x="15" y="21" width="4" height="3" fill="#fff"/><rect x="12" y="24" width="10" height="1.8" fill="#fff"/></svg></span>
      </li>
    </ul>

    <svg class="back-swoosh" viewBox="0 0 400 200" preserveAspectRatio="none" aria-hidden="true">
      <path d="M0 20 C40 10 70 0 110 6 C160 14 170 60 200 110 C225 150 250 180 290 200 L0 200 Z" fill="var(--navy)"/>
    </svg>
  </section>

</body>
</html>
```